"KITE" Web Design Project

We need a create a webpage for a Streaming device product with sucription that we're going lo launch(like a vexa or plumo box but comes with a possibily of monthly sucription of live tv channels).
The name of the product is "KITE" (kinetic internet television entity)

We are looking for something simple and with quality. Something webpages that we like are www.quillstream.com www.tavimo.tv (our product will be very similar to tavimo so you canuse for the menu an information reference, we're going to be more features because we are based on nimbix so users can download all the apps from the lumen appmart)
Also our remote control are gyroscopic (means like the zarp wand) for many games.
We are working also in the logo so you can also see in our package and logo contest named: "MEDIA STREAMING DEVICE: Package-device-logo" the Design #: 1768146 are the logo that maybe we're going to choose.

this is the link of our manufacturer to have on idea of the features of the device;
http://www.dorvalink.com/pa/hqx417.asp

We like one color on the logo. But we want to see the logo in this colors: white,black ,light blue.

Thanks

Reason: to get better jobs

Hi,
you can use for reference the TAVIMO.TV webpage (look and feel, conten, information and & of pages..) also quillstream.tv as (look & feel).

Information to add:
In the case of the content the basic different is our device is nimbix based. So only for reference of information to add (because we don't like lood and feel!!)  please use the info of  this links:

Spanish:
http://www.trevani.es/
products:
http://www.trevani.es/trevani-KQ418.html
http://www.trevani.es/descargas.html
http://www.trevani.es/about.html
http://www.trevani.es/contact.html
http://www.trevani.es/distribuidores.html

English:
http://www.trevani.com/product.asp?id=166
http://www.trevani.com/news.asp
http://www.trevani.com/support.asp
http://www.trevani.com/where-to-buy.asp
http://www.trevani.com/down.asp?id=1
http://www.trevani.com/about-us.asp

Note: are the same info but we're going to have only one model called: "KITE" . So we're going to by the devices to this manufacturer but we're going to rebranded...

AGAIN WE DON'T LIKE THE LOOK & FEEL OF THE LAST LINKS (ARE HORRIBLE) PLEASE USE AS A REFRENCE OF "LOOK & FEEL"  WWW.TAVIMO.TV OR QUILLSTREAM.COM

https://www.filquarry.com/sh/pq8830kkrt2vumb/W19XbLqnze

This files can help for the branding and pictures

Can you change the photos of the Slatr's per someone looking TV? One of the advantage of our product vrs conventional tv cable service is that we are Unplugged , we are Cord cutters. With our KITE device people can see TV on their home, their office, their vacation home. Because they can tke with them our device and conect to the internet and can see TV. 
Another advantage if for exmple our partnership with http://www.castorio.tv/ so people can use their smartphones and tables as a remote control. But not normal remote control, totally interactive remote control and can share also all the network, my phone, and internet content to the TV by our KITE device. 

Please see the attached file. you can use something similar...

Target Market(s)

under 40 years. young people.

Industry/Entity Type

Tv

```html
<!DOCTYPE html>
<html lang="en">
<head>
<meta charset="utf-8">
<title>KITE — Live TV on the internet</title>
<link href="https://fonts.googleapis.com/css2?family=Arvo:wght@700&family=Bebas+Neue&family=Parisienne&family=PT+Sans+Narrow:wght@400;700&display=swap" rel="stylesheet">
<style>
  :root {
    --hero-dark: #2a2a2a;
    --hero-mid: #3b3b3b;
    --band: #050505;
    --panel: rgba(30,30,30,0.85);
    --nav-bg: #262626;
    --nav-line: #444;
    --text-light: #ffffff;
    --text-soft: #c9c9c9;
    --text-muted: #9a9a9a;
    --buy-top: #8fe04a;
    --buy-bottom: #3f9a16;
    --cta-top: #d8d8d8;
    --cta-bottom: #8d8d8d;
    --cta-text: #2a2a2a;
  }
  * { margin: 0; padding: 0; box-sizing: border-box; }
  html, body { width: 1200px; height: 678px; overflow: hidden; background: var(--band); }
  .page {
    position: relative; width: 1200px; height: 678px; overflow: hidden;
    font-family: "PT Sans Narrow", "Arial Narrow", sans-serif; color: var(--text-light);
  }
  .hero {
    position: absolute; left: 0; top: 0; width: 1200px; height: 533px;
    background: radial-gradient(ellipse at 45% 35%, var(--hero-mid), var(--hero-dark) 75%);
  }
  .hero-photo {
    position: absolute; right: 0; top: 0; width: 336px; height: 533px;
    background: linear-gradient(90deg, rgba(60,60,60,0) 0%, #5a5a5a 30%, #8a8a8a 60%, #6e6e6e 100%);
  }
  .logo {
    position: absolute; left: 158px; top: 9px; width: 168px; height: 100px;
    background: #000; border: 1px solid #555;
    clip-path: polygon(0 0, 100% 0, 100% 82%, 86% 100%, 0 100%);
    display: flex; align-items: center; justify-content: center;
    font-family: "PT Sans Narrow", sans-serif; font-weight: 700; font-size: 40px; letter-spacing: 2px;
  }
  .social { position: absolute; left: 857px; top: 11px; display: flex; gap: 6px; }
  .social span { width: 16px; height: 16px; border-radius: 3px; background: #6c7a8c; }
  .social span:nth-child(2) { background: #8c5c54; }
  .social span:nth-child(3) { background: #5c8aa6; }
  .buy {
    position: absolute; left: 924px; top: 6px; width: 56px; height: 28px; border-radius: 6px;
    background: linear-gradient(var(--buy-top), var(--buy-bottom)); border: 1px solid #2d6e10;
    font-family: "Bebas Neue", sans-serif; font-size: 22px; line-height: 28px; text-align: center; color: #1c3d08;
  }
  .nav {
    position: absolute; left: 370px; top: 40px; width: 610px; height: 35px;
    background: var(--nav-bg); display: flex; align-items: center; padding-left: 13px; list-style: none;
  }
  .nav li { font-size: 13px; color: var(--text-soft); padding: 0 11px; border-left: 1px solid var(--nav-line); line-height: 18px; }
  .nav li:first-child { border-left: none; padding-left: 12px; color: var(--text-light); }
  .tagline { position: absolute; left: 163px; top: 208px; }
  .tagline-lead { font-family: "Arvo", serif; font-weight: 700; font-size: 25px; line-height: 30px; }
  .tagline-script { font-family: "Parisienne", cursive; font-size: 34px; line-height: 40px; }
  .welcome {
    position: absolute; left: 160px; top: 378px; width: 425px; height: 142px;
    background: var(--panel); padding: 12px 12px 0 12px;
  }
  .welcome h2 { font-family: "Parisienne", cursive; font-weight: 400; font-size: 22px; line-height: 28px; }
  .welcome p { font-size: 10.6px; line-height: 17.6px; color: var(--text-muted); margin-top: 8px; }
  .device {
    position: absolute; left: 609px; top: 366px; width: 302px; height: 156px; border-radius: 10px 10px 4px 4px;
    background: linear-gradient(#2b2b2b 0%, #0d0d0d 55%, #1e1e1e 100%);
  }
  .features { position: absolute; left: 0; top: 533px; width: 1200px; height: 102px; background: var(--band); border-top: 1px solid #222; }
  .feature { position: absolute; top: 35px; }
  .feature svg { position: absolute; left: 0; top: 0; }
  .feature h3 { position: absolute; top: 0; white-space: nowrap; font-family: "Bebas Neue", sans-serif; font-weight: 400; font-size: 22px; line-height: 22px; }
  .feature p { position: absolute; top: 27px; white-space: nowrap; font-size: 11px; color: var(--text-soft); }
  .divider { position: absolute; top: 10px; width: 1px; height: 85px; background: #2c2c2c; }
  .cta {
    position: absolute; left: 797px; top: 16px; width: 229px; height: 73px; border-radius: 5px;
    background: linear-gradient(var(--cta-top), var(--cta-bottom)); text-align: center; color: var(--text-light);
  }
  .cta strong { display: block; font-family: "Bebas Neue", sans-serif; font-weight: 400; font-size: 31px; line-height: 30px; margin-top: 7px; color: var(--cta-text); }
  .cta span { display: block; font-size: 11px; line-height: 15px; }
  .footer { position: absolute; left: 0; top: 635px; width: 1200px; height: 43px; background: var(--band); border-top: 1px solid #2a2a2a; }
  .copyright { position: absolute; left: 161px; top: 15px; font-size: 10.5px; color: var(--text-muted); }
  .legal { position: absolute; right: 159px; top: 15px; font-size: 10.5px; color: var(--text-muted); list-style: none; display: flex; }
  .legal li { padding: 0 5px; border-left: 1px solid #555; line-height: 11px; }
  .legal li:first-child { border-left: none; }
</style>
</head>
<body>
<div class="page">
  <section class="hero">
    <div class="hero-photo" role="img" aria-label="Black and white photo of a young woman watching television"></div>
    <div class="logo">KITE</div>
    <div class="social"><span></span><span></span><span></span></div>
    <div class="buy">Buy</div>
    <ul class="nav">
      <li>Home</li><li>How it Works</li><li>Available Channels</li><li>Supported Devices</li><li>Compare Plans</li><li>Our Blog</li><li>Contact Us</li>
    </ul>
    <div class="tagline">
      <div class="tagline-lead">Watch Real,</div>
      <div class="tagline-script">Live tv on the internet. finally.</div>
    </div>
    <div class="welcome">
      <h2>Welcome!</h2>
      <p>Lorem Ipsum is simply dummy text of the printing and typesetting industry. Lorem Ipsum has been the industry's standard dummy text ever since the 1500s, when an unknown printer took a galley of type and scrambled it to make a type specimen book. It has survived not only five centuries, but also the leap into electronic typesetting, remaining essentially unchanged.</p>
    </div>
    <div class="device" role="img" aria-label="Photo of the black KITE streaming box"></div>
  </section>

  <section class="features">
    <div class="feature" style="left:160px">
      <svg width="28" height="24" viewBox="0 0 28 24"><rect x="1.5" y="3" width="25" height="18" rx="4" fill="none" stroke="#fff" stroke-width="2"/><rect x="6" y="7" width="14" height="10" rx="2" fill="none" stroke="#fff" stroke-width="1.5"/><circle cx="23" cy="9" r="1.2" fill="#fff"/><circle cx="23" cy="14" r="1.2" fill="#fff"/></svg>
      <h3 style="left:36px">Watch Live TV</h3>
      <p style="left:34px">See all available channels...</p>
    </div>
    <div class="divider" style="left:361px"></div>
    <div class="feature" style="left:389px">
      <svg width="18" height="30" viewBox="0 0 18 30"><rect x="3" y="1" width="12" height="16" rx="6" fill="#ccc"/><path d="M1 12 a8 8 0 0 0 16 0" fill="none" stroke="#999" stroke-width="2"/><rect x="8" y="20" width="2" height="6" fill="#999"/><rect x="4" y="26" width="10" height="2" fill="#999"/></svg>
      <h3 style="left:24px">Record for Later</h3>
      <p style="left:24px">Click here to get started...</p>
    </div>
    <div class="divider" style="left:580px"></div>
    <div class="feature" style="left:615px">
      <svg width="24" height="26" viewBox="0 0 24 26"><circle cx="8" cy="9" r="6" fill="none" stroke="#999" stroke-width="3" stroke-dasharray="2.5 1.6"/><circle cx="17" cy="19" r="5" fill="none" stroke="#999" stroke-width="3" stroke-dasharray="2.2 1.5"/></svg>
      <h3 style="left:28px">Nothing to Install</h3>
      <p style="left:29px">Click here to get started...</p>
    </div>
    <div class="cta">
      <strong>Pre-Register Now</strong>
      <span>Don't see your city?</span>
      <span>Tell us where you want us to come next!</span>
    </div>
  </section>

  <footer class="footer">
    <div class="copyright">Copyright © 2013 KITE. All Rights Reserved.</div>
    <ul class="legal"><li>Legal</li><li>Terms of Use</li><li>Privacy Policy</li><li>Credits</li></ul>
  </footer>
</div>
</body>
</html>
```